Create a book cover for zorvex QPL

We are looking for a designer to design a cover for a log book in two versions. The two versions only have a slight difference in page count and text, other than that, it is one design.

The main color is blue. No black, no white except book title and other text. The cover must closely relate to the interior pages provided in the attachment. The style should be simple and modern, no old school graphics and fonts. Apply color psychology in the design. Please be creative and you are allowed to use download templates and graphic elements, but you must provide commercial licenses.

Here are the basic information of the book:
1. Book title: GARAGE SEASONS NOTE JOURNAL
2. Book size: 6x9 inches
3. Page count: 61 (version 1) and 73 (version 2)
4. Platform: zorvex qpl

Requirement for version 1:
1. Front cover: book title
2. Spine: no book title and author name
3. Back cover: text on the top and pen name logo on the bottom middle
4. Back cover text:
• Your essential tool for tracking vehicle health and maintenance
• Dedicated sections for maintenance schedules and repair history
• Track up to 30 maintenance schedules and repair history
• Easy-to-use tables and clear layouts
• Perfect for all car owners, from enthusiasts to everyday drivers

We hope it helps you keep your vehicle in excellent condition. Please take a moment to leave a positive review on Zorvex and share your experience if you find it helpful. Thank you!

Requirement for version 2:
1. Front cover: book title ,text "COLOR PAGES"
4. Back cover text:
• Track up to 36 maintenance schedules and repair history

Export:
1. Cover design in PDF and editable file format.
2. Sources/Commercial licenses for everything you did not create by yourself including fonts.

```html
<!DOCTYPE html>
<html lang="en">
<head>
<meta charset="utf-8">
<title>Garage Seasons Note Journal – Cover</title>
<link rel="stylesheet" href="https://fonts.googleapis.com/css2?family=Bebas+Neue&family=Oswald:wght@500&display=swap">
<style>
  :root {
    --page-bg: #ffffff;
    --cover-blue: #2b3b92;
    --cover-blue-light: #3b4ba0;
    --cover-blue-deep: #1b226e;
    --title-white: #f1f1f1;
    --title-yellow: #f5e717;
    --art-light: #b9bcc6;
    --art-dark: #6f7380;
    --badge-fill: #4a4f5c;
    --badge-ring: #9aa0ab;
    --badge-text: #e6e7ea;
  }
  html, body {
    margin: 0;
    padding: 0;
    width: 1200px;
    height: 1000px;
    overflow: hidden;
    background: var(--page-bg);
  }
  .canvas {
    display: block;
    width: 1200px;
    height: 1000px;
  }
  .cover-title {
    font-family: "Bebas Neue", "Oswald", sans-serif;
  }
  .title-white { fill: var(--title-white); }
  .title-yellow { fill: var(--title-yellow); }
  .pen-name {
    font-family: "Oswald", sans-serif;
    font-weight: 500;
    fill: var(--badge-text);
  }
</style>
</head>
<body>
<svg class="canvas" viewBox="0 0 1200 1000" xmlns="http://www.w3.org/2000/svg">
  <defs>
    <linearGradient id="coverGradient" x1="0" y1="0" x2="1" y2="0">
      <stop offset="0" stop-color="var(--cover-blue-light)"/>
      <stop offset="0.55" stop-color="var(--cover-blue)"/>
      <stop offset="1" stop-color="var(--cover-blue-deep)"/>
    </linearGradient>
    <linearGradient id="artGradient" x1="0" y1="0" x2="0" y2="1">
      <stop offset="0" stop-color="var(--art-light)"/>
      <stop offset="1" stop-color="var(--art-dark)"/>
    </linearGradient>
  </defs>

  <g class="front-cover">
    <rect class="cover-panel" x="340" y="85" width="545" height="830" fill="url(#coverGradient)"/>

    <rect class="tool-emblem" role="img"
          aria-label="Illustration of a piston with connecting rod over two crossed adjustable wrenches"
          x="652" y="405" width="198" height="168" rx="28"
          fill="url(#artGradient)"/>

    <g class="cover-title">
      <text class="title-white" x="365" y="285" font-size="202" textLength="490" lengthAdjust="spacingAndGlyphs">GARAGE</text>
      <text class="title-yellow" x="375" y="393" font-size="128" textLength="485" lengthAdjust="spacingAndGlyphs">SEASONS</text>
      <text class="title-yellow" x="373" y="565" font-size="210" textLength="260" lengthAdjust="spacingAndGlyphs">NOTE</text>
      <text class="title-white" x="370" y="722" font-size="190" textLength="450" lengthAdjust="spacingAndGlyphs">JOURNAL</text>
    </g>

    <g class="pen-name-badge">
      <circle cx="425" cy="797" r="50" fill="var(--badge-fill)" stroke="var(--badge-ring)" stroke-width="3"/>
      <text class="pen-name" x="425" y="804" font-size="17" text-anchor="middle">LEON VARDEK</text>
    </g>
  </g>
</svg>
</body>
</html>
```